Business Card Design Project

Hi Designers, this project is currently on hold until the Logo is completed:
Please submit to the Logo project here:
http://work.pitchvault.example/brief.aspx?id=413907

Once logo is completed, it will be attached to this project for you to create business cards with show logo, company name and address

Maren T R Quillby

Osric's Tiny Grey Heron Co.
Fernbrook
Nether Coombsby
North Devon EX91 4TZ

Tel: 01809 417356
Mobile: 07900 263818
email: maren@tiny-grey-heron.example.co.uk

Project Deadline Extended
Reason: Sorry everyone, we have had a sick ewe and I am now behind with this one and need to extend the deadline. Best wishes Maren

The designer who wins the logo brief will be asked to design the business card. Many thanks Maren

Project Deadline Extended
Reason: Sorry everyone, just a chaotic time of year with animals. Need to extend the deadline again..... as I just haven't had enough time to take a good look.... Thank you for your understanding. Maren

Project Deadline Extended
Reason: Sorry everyone It is our busiest time of year with animals and just no time to spend going through such great designs. I will have to extend the deadline again and hopefully have some news very soon. Wishing you all a very happy Christmas and a happy and healthy new year. Maren & Osric

High end market
Boutique restaurants for meat (it's not commercial lamb it's a slow matured quality meat more like venison/beef) expensive - specialized market

High End shoot clothing / wool / sheepskin rugs
Quality products

Business

• based on the logo - (which Pitch Vault has just been asked to do)
possibly based on a simplified picture of a Hebridean Ram (shows it's a Hebridean by it's horns as opposed to other black sheep!!)

```html
<!DOCTYPE html>
<html lang="en">
<head>
<meta charset="utf-8">
<title>Business Card – Maren T R Quillby</title>
<link href="https://fonts.googleapis.com/css2?family=Arimo:wght@400&family=Tinos:wght@400;700&display=swap" rel="stylesheet">
<style>
  :root {
    --backdrop: #d9d3c9;
    --card: #252a2a;
    --ink: #ffffff;
    --ink-soft: #e6e6e6;
    --mark-ring: #ffffff;
    --mark-faint: #5b5f5f;
  }
  html, body {
    margin: 0;
    padding: 0;
    width: 1200px;
    height: 870px;
    overflow: hidden;
    background: var(--backdrop);
  }
  .stage {
    width: 1200px;
    height: 870px;
    display: flex;
    align-items: center;
    justify-content: center;
    gap: 60px;
  }
  .card {
    position: relative;
    width: 500px;
    height: 780px;
    background: var(--card);
    color: var(--ink);
    box-sizing: border-box;
    overflow: hidden;
    font-family: "Tinos", "Times New Roman", serif;
  }
  .card-front {
    padding: 70px 30px 0 60px;
  }
  .brand {
    display: flex;
    flex-direction: column;
    align-items: center;
    text-align: center;
  }
  .brand-dot {
    width: 150px;
    height: 150px;
    border-radius: 50%;
    border: 10px solid var(--mark-ring);
    box-sizing: border-box;
  }
  .brand-name {
    margin-top: 22px;
    font-size: 26px;
    font-weight: 400;
    letter-spacing: 1px;
    color: var(--ink);
    line-height: 1.2;
  }
  .person {
    margin-top: 110px;
  }
  .person-name {
    font-size: 34px;
    font-weight: 700;
    margin: 0;
    line-height: 1.1;
  }
  .person-role {
    font-family: "Arimo", Arial, sans-serif;
    font-size: 17px;
    color: var(--ink-soft);
    margin: 4px 0 0 6px;
  }
  .contact {
    list-style: none;
    margin: 70px 0 0 0;
    padding: 0;
  }
  .contact-item {
    display: flex;
    align-items: center;
    font-size: 19px;
    line-height: 1.25;
    margin-bottom: 26px;
    white-space: nowrap;
  }
  .contact-icon {
    width: 24px;
    height: 24px;
    flex: none;
    margin-right: 36px;
    fill: var(--ink);
  }
  .card-back .watermark {
    position: absolute;
    top: -60px;
    right: -110px;
    width: 420px;
    height: 420px;
    border-radius: 50%;
    border: 30px solid var(--mark-faint);
    box-sizing: border-box;
  }
  .card-back .brand {
    position: absolute;
    left: 0;
    right: 0;
    top: 430px;
  }
</style>
</head>
<body>
<main class="stage">
  <article class="card card-front">
    <header class="brand">
      <div class="brand-dot" aria-hidden="true"></div>
      <div class="brand-name">Osric's Tiny Grey Heron Co.</div>
    </header>

    <section class="person">
      <h1 class="person-name">Maren T R Quillby</h1>
      <p class="person-role">Managing Director</p>
    </section>

    <ul class="contact">
      <li class="contact-item">
        <svg class="contact-icon" viewBox="0 0 24 24" aria-label="Telephone">
          <path d="M3 9c0-3 4-5 9-5s9 2 9 5v1h-5V8c-1-.6-2.5-1-4-1s-3 .4-4 1v2H3z"/>
          <path d="M7 11h10l3 8H4z"/>
        </svg>
        <span>01809 417356</span>
      </li>
      <li class="contact-item">
        <svg class="contact-icon" viewBox="0 0 24 24" aria-label="Mobile">
          <rect x="7" y="2" width="10" height="20" rx="2"/>
          <rect x="9" y="5" width="6" height="6" fill="#252a2a"/>
        </svg>
        <span>07900 263818</span>
      </li>
      <li class="contact-item">
        <svg class="contact-icon" viewBox="0 0 24 24" aria-label="Address">
          <path d="M12 2 2 11h3v10h5v-6h4v6h5V11h3z"/>
        </svg>
        <span>Fernbrook Nether Coombsby<br>North Devon EX91 4TZ</span>
      </li>
      <li class="contact-item">
        <svg class="contact-icon" viewBox="0 0 24 24" aria-label="Email">
          <path d="M2 5h20v14H2z"/>
          <path d="M3 6l9 7 9-7" fill="none" stroke="#252a2a" stroke-width="1.6"/>
        </svg>
        <span>maren@tiny-grey-heron.example.co.uk</span>
      </li>
    </ul>
  </article>

  <article class="card card-back">
    <div class="watermark" aria-hidden="true"></div>
    <header class="brand">
      <div class="brand-dot" aria-hidden="true"></div>
      <div class="brand-name">Osric's Tiny Grey Heron Co.</div>
    </header>
  </article>
</main>
</body>
</html>
```